Vortique Energy Business Card Design

website: www.vortiqueenergy.example
Project: Business Card Design for Vortique Energy
Name: Derek Holloway
Title: Founder / Operations Strategist
Visual Identity & Logo:
Logo File: VRT-Logo-FullGradient-Final.png (Attached).
Color Palette: The brand relies on a distinctive Cyan (Blue) to Lime Green gradient.
Background Preference: We want a Dark Mode aesthetic (Deep Matte Black, Charcoal, or Dark Slate) to make the neon gradient of the logo pop. This feels more "tech/industrial" than a standard white card.
Design Aesthetic (The "Ops" Vibe):
Concept: "Grid & Infrastructure." We are a solar rental company, focusing on logistics and access.
Typography: White, bold sans-serif text for contact info. High contrast against the dark background.
Accents: Use the Cyan or Lime Green from the logo for thin divider lines or edge painting.
Avoid: No orange/gold (clashes with logo). No cartoon leaves.
Layout Requirements:
Front: Large, centered logo. Maybe a subtle UV gloss spot varnish over the logo icon.
Back: Name, Title, Contact Info.
Texture: Matte finish cardstock with gloss elements.
sample mock up of information on card: https://brimtolcorp-my.filedock.example/:i:/g/personal/derek_holloway_vortiqueenergy_com/AbCdEfGhIjKlMnOpQrStUvWxYz0123456789AbCdEfGh?e=X1Y2Z3
Logo: https://brimtolcorp.filedock.example/:i:/s/VortiqueEnergy/ZyXwVuTsRqPoNmLkJiHgFeDcBa9876543210ZyXwVuTs?e=Q4R5S6

```html
<!DOCTYPE html>
<html lang="en">
<head>
<meta charset="utf-8">
<title>Vortique Energy – Business Card</title>
<link href="https://fonts.googleapis.com/css2?family=Quicksand:wght@500;600;700&display=swap" rel="stylesheet">
<style>
  :root {
    --stage: #d9cfc3;
    --charcoal: #2b2c2e;
    --matte-black: #141414;
    --cyan: #1fb3c9;
    --lime: #8cc63f;
    --white: #f2f2f2;
  }
  * { box-sizing: border-box; margin: 0; padding: 0; }
  html, body { width: 1200px; height: 900px; overflow: hidden; }
  body {
    background: var(--stage);
    font-family: "Quicksand", sans-serif;
    position: relative;
  }
  .card {
    position: absolute;
    width: 560px;
    height: 320px;
    border-radius: 26px;
    overflow: hidden;
    box-shadow: 0 14px 30px rgba(0, 0, 0, 0.28);
  }
  .card--details { left: 320px; top: 100px; background: var(--charcoal); }
  .card--brand {
    left: 320px; top: 480px;
    background: radial-gradient(ellipse at 50% 40%, #262626 0%, var(--matte-black) 70%);
  }

  /* back: contact details */
  .holder { position: absolute; left: 34px; top: 44px; }
  .holder__name {
    color: var(--lime);
    font-weight: 600;
    font-size: 19px;
    letter-spacing: 0.5px;
    text-transform: uppercase;
  }
  .holder__title { color: var(--white); font-weight: 500; font-size: 15px; margin-top: 2px; }

  .contact { position: absolute; left: 300px; top: 34px; width: 230px; }
  .contact__company { color: var(--cyan); font-weight: 600; font-size: 15px; }
  .contact__address { color: var(--white); font-size: 13.5px; line-height: 1.35; font-weight: 500; }
  .contact__label { color: var(--cyan); font-weight: 600; font-size: 14px; margin-top: 8px; }
  .offices { display: flex; gap: 6px; margin-top: 4px; }
  .offices svg { width: 20px; height: 20px; }
  .contact__line {
    display: flex; align-items: center; gap: 7px;
    color: var(--white); font-size: 13.5px; font-weight: 500; margin-top: 6px;
  }
  .contact__line + .contact__line { margin-top: 2px; }
  .contact__line svg { width: 13px; height: 13px; flex: none; }
  .contact__rule { height: 1px; background: var(--lime); margin-top: 8px; width: 230px; }

  .wordmark {
    display: flex; align-items: center; gap: 10px;
    color: var(--cyan); font-weight: 600; white-space: nowrap;
  }
  .wordmark__square { background: var(--cyan); border-radius: 3px; flex: none; }
  .card--details .wordmark { position: absolute; left: 300px; top: 248px; font-size: 26px; }
  .card--details .wordmark__square { width: 26px; height: 26px; }

  /* front: centred brand */
  .brand-lockup {
    position: absolute; left: 0; right: 0; top: 108px;
    display: flex; flex-direction: column; align-items: center;
  }
  .card--brand .wordmark { font-size: 40px; }
  .card--brand .wordmark__square { width: 38px; height: 38px; }
  .brand-lockup__rule { width: 330px; height: 1px; background: var(--lime); margin-top: 10px; }
  .brand-lockup__tagline {
    color: var(--white); font-size: 14px; font-weight: 600; margin-top: 10px; letter-spacing: 0.2px;
  }
</style>
</head>
<body>

<section class="card card--details" aria-label="Card back with contact details">
  <div class="holder">
    <p class="holder__name">Derek Holloway</p>
    <p class="holder__title">Founder / Operations Strategist</p>
  </div>

  <div class="contact">
    <p class="contact__company">Vortique Energy</p>
    <p class="contact__address">4120 Harbor Crest Lane<br>Orlando, FL 32811</p>
    <p class="contact__label">Offices</p>
    <div class="offices">
      <svg viewBox="0 0 20 20" role="img" aria-label="United States office flag"><circle cx="10" cy="10" r="9.5" fill="#c8303b"/><circle cx="10" cy="10" r="6" fill="#f4f4f4"/><circle cx="10" cy="10" r="3" fill="#2a3f8f"/></svg>
      <svg viewBox="0 0 20 20" role="img" aria-label="United Kingdom office flag"><circle cx="10" cy="10" r="9.5" fill="#22357a"/><rect x="8" y="0.5" width="4" height="19" fill="#d8283a"/><rect x="0.5" y="8" width="19" height="4" fill="#d8283a"/></svg>
      <svg viewBox="0 0 20 20" role="img" aria-label="Canada office flag"><circle cx="10" cy="10" r="9.5" fill="#f4f4f4"/><circle cx="10" cy="10" r="4" fill="#d52b1e"/></svg>
    </div>
    <p class="contact__line">
      <svg viewBox="0 0 24 24" aria-hidden="true"><path fill="#1fb3c9" d="M6.6 10.8a15 15 0 0 0 6.6 6.6l2.2-2.2c.3-.3.7-.4 1-.2 1.1.4 2.3.6 3.6.6.6 0 1 .4 1 1V20c0 .6-.4 1-1 1A17 17 0 0 1 3 4c0-.6.4-1 1-1h3.5c.6 0 1 .4 1 1 0 1.3.2 2.5.6 3.6.1.3 0 .7-.2 1z"/></svg>
      555.014.2290
    </p>
    <p class="contact__line">
      <svg viewBox="0 0 24 24" aria-hidden="true"><circle cx="12" cy="12" r="10" fill="none" stroke="#1fb3c9" stroke-width="2"/><path d="M2 12h20M12 2c3 3 3 17 0 20M12 2c-3 3-3 17 0 20" fill="none" stroke="#1fb3c9" stroke-width="1.6"/></svg>
      www.vortiqueenergy.example
    </p>
    <div class="contact__rule"></div>
  </div>

  <div class="wordmark"><span class="wordmark__square" aria-hidden="true"></span>Vortique Energy</div>
</section>

<section class="card card--brand" aria-label="Card front with brand name">
  <div class="brand-lockup">
    <div class="wordmark"><span class="wordmark__square" aria-hidden="true"></span>Vortique Energy</div>
    <div class="brand-lockup__rule"></div>
    <p class="brand-lockup__tagline">Clean Power, Zero Upfront, Fully Managed Care.</p>
  </div>
</section>

</body>
</html>
```